Verdant Pathworks Business Card

want the back of card to be blue- with the logo in the center
front of card- info plus logo (info being mailing address, email address, and website address )
4 different names with titles to have on cards
1) Dominic Ashvale - Owner
2) Bethany Korvuth- Customer Relationship Specialist
3) Luca Brennwick- Vice President of Sales
4) Neil Umbright- Chief Technology Officer

Target Market(s)

tech company in the government/probation office industry

Industry/Entity Type

Government Office

Contact Information for Business Card

1) Dominic Ashvale - Owner

Colors
0355a3
ffffff

Requirements
Must have
• back side should be blue, with the logo placed in the center
• front side needs to include both the logo, as well as company info (info should include website address, email address, and mailing address)

```html
<!DOCTYPE html>
<html lang="en">
<head>
<meta charset="utf-8">
<title>Verdant Pathworks Business Card</title>
<link href="https://fonts.googleapis.com/css2?family=Roboto:wght@400;500&family=Noto+Serif:wght@400&display=swap" rel="stylesheet">
<style>
  :root {
    --navy: #25396c;
    --navy-deep: #1a2a52;
    --white: #ffffff;
    --grey-band: #8f8f99;
    --grey-text: #7a7a82;
    --paper: #fbfbfb;
    --backdrop: #a19e9e;
  }
  html, body {
    margin: 0;
    padding: 0;
    width: 1200px;
    height: 1200px;
    overflow: hidden;
    background: var(--backdrop);
  }
  .canvas {
    position: relative;
    width: 1200px;
    height: 1200px;
  }
  .card {
    position: absolute;
    width: 712px;
    height: 416px;
    background: var(--paper);
    border-radius: 22px;
    overflow: hidden;
    font-family: "Roboto", Arial, sans-serif;
  }
  .card--brand { left: 238px; top: 120px; background: var(--navy); }
  .card--contact { left: 231px; top: 645px; }

  .wordmark {
    position: absolute;
    display: flex;
    align-items: center;
    gap: 14px;
    color: var(--navy);
    font-family: "Roboto", Arial, sans-serif;
    font-weight: 500;
    white-space: nowrap;
  }
  .wordmark__square {
    background: currentColor;
    flex: none;
  }
  .card--brand .wordmark {
    left: 0; right: 0;
    top: 170px;
    justify-content: center;
    font-size: 54px;
    letter-spacing: 1px;
    color: var(--white);
  }
  .card--brand .wordmark__square { width: 30px; height: 30px; }

  .brand-site {
    position: absolute;
    left: 0; right: 0;
    top: 374px;
    display: flex;
    justify-content: center;
    align-items: center;
    gap: 22px;
    color: var(--white);
    font-size: 18px;
  }
  .brand-site__dash {
    width: 46px;
    height: 3px;
    background: var(--white);
    border-radius: 2px;
  }
  .split-band {
    position: absolute;
    left: 0; right: 0; bottom: 0;
    height: 15px;
    display: flex;
  }
  .split-band__navy { flex: 357; background: var(--navy-deep); }
  .split-band__grey { flex: 355; background: var(--grey-band); }

  .person {
    position: absolute;
    left: 31px;
    top: 62px;
  }
  .person__name {
    margin: 0;
    font-family: "Noto Serif", Georgia, serif;
    font-weight: 400;
    font-size: 25px;
    letter-spacing: 0.5px;
    color: var(--navy);
    text-transform: uppercase;
  }
  .person__title {
    margin: 4px 0 0;
    font-size: 17px;
    color: var(--grey-text);
  }
  .card--contact .wordmark {
    right: 32px;
    top: 120px;
    font-size: 35px;
    gap: 10px;
  }
  .card--contact .wordmark__square { width: 20px; height: 20px; }

  .details {
    position: absolute;
    left: 31px;
    top: 259px;
    color: var(--grey-text);
    font-size: 17px;
    line-height: 29px;
  }
  .details p { margin: 0; }
  .details__line {
    display: flex;
    align-items: center;
    gap: 18px;
    line-height: 27px;
  }
  .details__address { margin-bottom: 5px !important; }
  .details__line svg { width: 19px; height: 19px; fill: var(--navy); flex: none; }

  .contact-footer {
    position: absolute;
    left: 0; bottom: 0;
    width: 712px;
    height: 52px;
  }
  .contact-footer__site {
    position: absolute;
    right: 32px;
    bottom: 16px;
    color: var(--white);
    font-size: 17px;
    letter-spacing: 0.3px;
  }
</style>
</head>
<body>
<div class="canvas">

  <section class="card card--brand">
    <div class="wordmark">
      <span class="wordmark__square"></span>
      <span class="wordmark__name">Verdant Pathworks</span>
    </div>
    <div class="brand-site">
      <span class="brand-site__dash"></span>
      <span>www.verdantpathworks.com</span>
      <span class="brand-site__dash"></span>
    </div>
    <div class="split-band">
      <span class="split-band__navy"></span>
      <span class="split-band__grey"></span>
    </div>
  </section>

  <section class="card card--contact">
    <div class="person">
      <h1 class="person__name">Bethany Korvuth</h1>
      <p class="person__title">Customer Relationship Specialist</p>
    </div>

    <div class="wordmark">
      <span class="wordmark__square"></span>
      <span class="wordmark__name">Verdant Pathworks</span>
    </div>

    <div class="details">
      <p class="details__address">234 Anywhere St., Any City,<br>Any Town, US 123456</p>
      <p class="details__line">
        <svg viewBox="0 0 24 24" aria-hidden="true"><path d="M3 9c0-3 4-5 9-5s9 2 9 5v2h-5V9c-1-.6-2.4-1-4-1s-3 .4-4 1v2H3V9zm3 4h12l2 7H4l2-7zm6 1.5a2.5 2.5 0 1 0 0 5 2.5 2.5 0 0 0 0-5z"/></svg>
        <span>111-111-1111</span>
      </p>
      <p class="details__line">
        <svg viewBox="0 0 24 24" aria-hidden="true"><path d="M2 5h20v14H2V5zm2 2v.4l8 5.6 8-5.6V7H4zm0 2.8V17h16V9.8l-8 5.6-8-5.6z"/></svg>
        <span>bethany.k@verdantpathworks.com</span>
      </p>
    </div>

    <svg class="contact-footer" viewBox="0 0 712 52" aria-hidden="true">
      <rect x="0" y="37" width="712" height="15" fill="#8f8f99"/>
      <path d="M392 2 H712 V52 H366 Z" fill="#25396c"/>
    </svg>
    <span class="contact-footer__site">www.verdantpathworks.com</span>
  </section>

</div>
</body>
</html>
```